Epoxy Flooring Contractor business card

We need a business card to promote a new addition to our business. We now offer Epoxy Flooring. We would like for the business card to include the images attached. One is our logo, the other is a sample of metallic epoxy flooring, we would like to incorporate that somewhere into the design. I was thinking an icon of a man pushing a concrete grinder and have the color set to the metallic epoxy color. I found a business card sample on this website, I will attach it. It has the icon that we are looking for, or something similar.
Our company name is Brightmore Coatings LLC
Our owners name is Dana Pellow
Phone is 555-847-2916
website is www.brightmore-coatingsllc.com
please let me know if you need any other info

Contact Information for Business Card

Brightmore Coatings LLC
Dana Pellow, owner
Phone: 555-847-2916
Address: P.O Box 8146 Cedar Hollow, OR 97841
www.Brightmore-CoatingsLLC.com
BrightmoreCoatingsLLC@mailvista.net
Include logo attached
It must include a Clip art of man with concrete grinder
Must include metallic epoxy design attached
Must include the following text
Residential Garage Flooring
Epoxy Countertops
Commercial Epoxy Flooring
Restaurant Flooring
Warehouse Flooring
Licensed & Insured
Free Estimates

Colors

Designer to choose colors to be used in the design.

Requirements
Must have
• Include logo attached
• It must include a Clip art of man with concrete grinder
• Must include metallic epoxy design attached
• Must include the following text
• Garage Epoxy Flooring
• Residential Epoxy Flooring
• Concrete Floor Crack Repairs
• Concrete Floor Grinding
• Commercial & Warehouse Epoxy Flooring
• Restaurant Epoxy Flooring
• Epoxy Countertops
• Non Slip Epoxy Pool Decks
• Textured Finishes, Flakes, Granite Coat, Metallic & Quartz
• FREE ESTIMATES • LICENSED & INSURED

```html
<!DOCTYPE html>
<html lang="en">
<head>
<meta charset="utf-8">
<title>Brightmore Coatings LLC – Business Card</title>
<link href="https://fonts.googleapis.com/css2?family=Open+Sans:wght@400;600;700&display=swap" rel="stylesheet">
<style>
  :root {
    --backdrop: #3b3c3f;
    --card-white: #fbf7f7;
    --blue-light: #79a6d6;
    --blue-mid: #5b86b9;
    --blue-dark: #3f6591;
    --navy: #2f5583;
    --ink-grey: #4a4a4a;
    --white: #ffffff;
  }
  * { box-sizing: border-box; margin: 0; padding: 0; }
  html, body {
    width: 1200px; height: 782px; overflow: hidden;
    background: var(--backdrop);
    font-family: "Open Sans", Arial, sans-serif;
  }
  .stage {
    position: relative; width: 1200px; height: 782px;
    display: flex; align-items: center; justify-content: center; gap: 40px;
  }
  .card {
    position: relative; width: 540px; height: 309px; overflow: hidden;
    box-shadow: 0 10px 24px rgba(0,0,0,.45);
  }

  /* Front */
  .card-front { background: var(--card-white); }
  .card-front .bands { position: absolute; inset: 0; }
  .name-block { position: absolute; left: 50px; top: 32px; }
  .name { font-size: 24px; font-weight: 700; line-height: 1; }
  .name .first { color: var(--blue-mid); }
  .name .last { color: var(--navy); }
  .role { font-size: 11px; color: var(--ink-grey); margin-top: 2px; }
  .contacts { position: absolute; left: 22px; top: 176px; list-style: none; }
  .contacts li {
    display: flex; align-items: center; gap: 6px;
    font-size: 13px; color: var(--ink-grey); line-height: 18px;
  }
  .contacts svg { width: 11px; height: 11px; fill: var(--navy); flex: none; }
  .brand-lockup {
    position: absolute; left: 300px; top: 140px;
    display: flex; align-items: center; gap: 10px;
  }
  .brand-lockup .mark { width: 18px; height: 18px; background: var(--blue-mid); }
  .brand-lockup .wordmark {
    font-size: 22px; font-weight: 600; color: var(--ink-grey); line-height: 1.05;
  }
  .company { position: absolute; right: 40px; top: 200px; text-align: right; }
  .company .legal { font-size: 14px; font-weight: 700; color: var(--navy); }
  .company .address { font-size: 14px; color: var(--ink-grey); line-height: 18px; }

  /* Back */
  .card-back {
    background: linear-gradient(120deg, var(--blue-dark) 0%, var(--blue-light) 40%, var(--blue-mid) 70%, var(--blue-dark) 100%);
  }
  .card-back .pattern-field {
    position: absolute; inset: 0;
    background: linear-gradient(120deg, rgba(255,255,255,.05), rgba(255,255,255,.14) 45%, rgba(255,255,255,.04));
  }
  .back-lockup {
    position: absolute; right: 60px; top: 118px;
    display: flex; align-items: center; gap: 8px;
  }
  .back-lockup .mark { width: 14px; height: 14px; background: var(--white); }
  .back-lockup .wordmark { font-size: 20px; font-weight: 700; color: var(--white); }
  .services {
    position: absolute; right: 28px; bottom: 40px; text-align: right;
    color: var(--white); font-size: 13.5px; line-height: 19px;
  }
</style>
</head>
<body>
<main class="stage">

  <section class="card card-front" aria-label="Business card front">
    <svg class="bands" viewBox="0 0 540 309" aria-hidden="true">
      <polygon points="0,38 14,38 14,62 0,62" fill="var(--blue-light)"/>
      <polygon points="22,38 40,38 30,62 12,62" fill="var(--navy)"/>
      <polygon points="0,262 306,262 296,280 0,280" fill="var(--blue-light)"/>
      <polygon points="306,270 540,270 540,309 284,309" fill="var(--blue-dark)"/>
    </svg>

    <div class="name-block">
      <p class="name"><span class="first">Dana</span> <span class="last">Pellow</span></p>
      <p class="role">Owner</p>
    </div>

    <ul class="contacts">
      <li><svg viewBox="0 0 24 24"><path d="M6.6 10.8a15.1 15.1 0 0 0 6.6 6.6l2.2-2.2c.3-.3.7-.4 1-.2 1.1.4 2.3.6 3.6.6.6 0 1 .4 1 1V20c0 .6-.4 1-1 1A17 17 0 0 1 3 4c0-.6.4-1 1-1h3.5c.6 0 1 .4 1 1 0 1.3.2 2.5.6 3.6.1.3 0 .7-.2 1z"/></svg>555-847-2916</li>
      <li><svg viewBox="0 0 24 24"><path d="M2 5h20v14H2z M2 5l10 8 10-8" fill="none" stroke="var(--navy)" stroke-width="2.5"/></svg>BrightmoreCoatingsLLC@mailvista.net</li>
      <li><svg viewBox="0 0 24 24"><circle cx="12" cy="12" r="10"/></svg>www.Brightmore-CoatingsLLC.com</li>
    </ul>

    <div class="brand-lockup">
      <span class="mark"></span>
      <span class="wordmark">Brightmore<br>Coatings</span>
    </div>

    <div class="company">
      <p class="legal">Brightmore Coatings LLC</p>
      <p class="address">P.O Box 8146 Cedar<br>Hollow, OR 97841</p>
    </div>
  </section>

  <section class="card card-back" aria-label="Business card back">
    <div class="pattern-field" role="img" aria-label="Faint repeating brand pattern across the card"></div>
    <div class="back-lockup">
      <span class="mark"></span>
      <span class="wordmark">Brightmore Coatings</span>
    </div>
    <p class="services">
      Residential Garage Flooring • Epoxy Countertops<br>
      Commercial Epoxy Flooring • Restaurant Flooring<br>
      Warehouse Flooring • Licensed &amp; Insured • Free Estimates
    </p>
  </section>

</main>
</body>
</html>
```